I need this done FAST!
Business Cards and Stationary for new home construction company - Construction
Simple
Gerald Finch
Owner
4816 Marlow Ct #306142 Houston, TX 77391
Gerald@thequillstoneframeworks.com
www.thequillstoneframeworks.com
I would like this business card to be minimal in its design. I just want it to be a way of saying ... Hi, call me directly. It does not need to be an advertisement. I need the vector files of this please
Front should be the logo only, and the back should be this information: Design~Build Firm Gerald Finch, Owner Phone Email Web address

```html
<!DOCTYPE html>
<html lang="en">
<head>
<meta charset="utf-8">
<title>Quillstone Frameworks – Business Card</title>
<link href="https://fonts.googleapis.com/css2?family=Open+Sans:wght@400;600;700&display=swap" rel="stylesheet">
<style>
  :root {
    --backdrop: #e4e4e6;
    --card: #ffffff;
    --ink: #2b2b2b;
    --ink-soft: #4a4a4a;
    --accent: #d81f26;
    --accent-dark: #a3141a;
    --pill: #b9b9bb;
    --pill-text: #ffffff;
  }
  * { box-sizing: border-box; margin: 0; padding: 0; }
  html, body {
    width: 1200px; height: 816px; overflow: hidden;
    background: var(--backdrop);
    font-family: "Open Sans", Arial, sans-serif;
  }
  .card {
    position: absolute; left: 75px; top: 108px;
    width: 1050px; height: 600px;
    background: var(--card);
    border-radius: 34px;
    overflow: hidden;
    box-shadow: 0 10px 30px rgba(0,0,0,.15);
  }
  .card__band {
    position: absolute; left: 0; right: 0; bottom: 0; height: 46px;
    background: linear-gradient(180deg, var(--accent) 0%, var(--accent-dark) 100%);
  }
  .identity { position: absolute; left: 70px; top: 205px; }
  .identity__name {
    font-size: 36px; font-weight: 700; color: var(--ink);
    letter-spacing: .5px; text-transform: uppercase;
  }
  .identity__role { font-size: 26px; color: var(--ink-soft); margin-top: 4px; }
  .contacts { position: absolute; left: 70px; top: 345px; list-style: none; }
  .contacts__item {
    display: flex; align-items: flex-start; gap: 14px;
    font-size: 23px; line-height: 30px; color: var(--ink); margin-bottom: 4px;
  }
  .contacts__item--address { font-weight: 700; }
  .contacts__icon { width: 20px; height: 20px; margin-top: 5px; flex: none; fill: var(--ink); }
  .brand {
    position: absolute; left: 640px; top: 150px;
    display: flex; align-items: center; gap: 16px;
  }
  .brand__mark { width: 34px; height: 34px; background: var(--accent); flex: none; }
  .brand__name {
    font-size: 40px; font-weight: 700; color: var(--accent); line-height: 1.05;
  }
  .web-pill {
    position: absolute; left: 560px; right: 0; top: 300px; height: 62px;
    background: var(--pill);
    border-radius: 31px 0 0 31px;
    display: flex; align-items: center;
    padding: 0 28px 0 34px;
    color: var(--pill-text); font-size: 22px; font-weight: 600;
    white-space: nowrap;
  }
</style>
</head>
<body>
  <div class="card">
    <div class="brand">
      <span class="brand__mark"></span>
      <span class="brand__name">Quillstone<br>Frameworks</span>
    </div>
    <div class="web-pill">www.thequillstoneframeworks.com</div>

    <div class="identity">
      <h1 class="identity__name">Gerald Finch</h1>
      <p class="identity__role">Owner</p>
    </div>

    <ul class="contacts">
      <li class="contacts__item contacts__item--address">
        <svg class="contacts__icon" viewBox="0 0 20 20"><path d="M10 1a6 6 0 0 0-6 6c0 4.5 6 12 6 12s6-7.5 6-12a6 6 0 0 0-6-6zm0 8.3A2.3 2.3 0 1 1 10 4.7a2.3 2.3 0 0 1 0 4.6z"/></svg>
        <span>4816 Marlow Ct #306142<br>Houston, TX 77391</span>
      </li>
      <li class="contacts__item">
        <svg class="contacts__icon" viewBox="0 0 20 20"><path d="M2 6c0-2 2-3 3-3h10c1 0 3 1 3 3v1h-4V5H6v2H2zm2 3h12l2 8H2zm6 2a2.5 2.5 0 1 0 0 5 2.5 2.5 0 0 0 0-5z"/></svg>
        <span>713 555 0142</span>
      </li>
      <li class="contacts__item">
        <svg class="contacts__icon" viewBox="0 0 20 20"><path d="M6 1h8a1.5 1.5 0 0 1 1.5 1.5v15A1.5 1.5 0 0 1 14 19H6a1.5 1.5 0 0 1-1.5-1.5v-15A1.5 1.5 0 0 1 6 1zm0 2.5v11h8v-11zM10 15.5a1 1 0 1 0 0 2 1 1 0 0 0 0-2z"/></svg>
        <span>713 555 0187</span>
      </li>
      <li class="contacts__item">
        <svg class="contacts__icon" viewBox="0 0 20 20"><path d="M1 4h18v12H1zm2 2v.5l7 4.5 7-4.5V6l-7 4.5z"/></svg>
        <span>Gerald@thequillstoneframeworks.com</span>
      </li>
    </ul>

    <div class="card__band"></div>
  </div>
</body>
</html>
```